Cambodia 501c3 flyer design

I need a flyer to build interest and awareness for a school year kick off event in October for our charity school in rural Cambodia. I have text and photos available and just need help getting a professional look and feel. (Other projects may follow, including logo and web redesign.)

Founded in 2004 by Lars Movik, The Riverside Learning House at Tonle Prey is a 501(c)(3) organization dedicated to breaking the cycle of poverty of some of Cambodia's poorest children by providing a rigorous core K-9 education that emphasizes English proficiency.

"The board of directors of The Riverside Learning House at Tonle Prey invites you to our annual visit to Tonle Prey, Cambodia to help launch the new school year. The trip is open to everyone-you do not need to be a current donor to attend.

If you have been interested in visiting an educational project that works for hundreds of the poorest children in Cambodia, here is your chance. This school is a lifeline for these children and their families, providing education, transportation, uniforms, and two meals a day."
Updates

Hi everyone! I am really impressed by these designs and there are some really promising directions. One thing I would like to see is revisions with more white space, with the blues and yellows as more accents. Any sort of conservative sans serif font is fine.

Also, in general I will need the final in some kind of editable format where I can make basic text updates. I can do this with either AI or Word. 

The use of the kids' photos is great! I will issue a preliminary cut in the next few days. Thank you all again very much for your work on the behalf of the school and children of Cambodia!

Reason: Hi all, I am going to extend the deadline by 7 days so that I have a chance to review the comps with the other board members. That meeting takes place on 21 April so I should be able to proceed shortly thereafter.

Target Market(s)

For this piece, current donors and prospective donors

Industry/Entity Type

Education

Requirements
Nice to have
• Use any elements from www.riversidelearnhouse.org as you see fit. There are lots of photos of the students that might be helpful. There are also more photos of the school at my Flickr account at
http://www.photoshelfhub.com/photos/58172046@K07/page4/

```html
<!DOCTYPE html>
<html lang="en">
<head>
<meta charset="utf-8">
<title>2013 School Year Kick Off Tour</title>
<link rel="stylesheet" href="https://fonts.googleapis.com/css2?family=Jost:wght@400;500;700&family=Cinzel:wght@500&display=swap">
<style>
  :root {
    --green: #3f9a3a;
    --blue: #2f80c6;
    --red: #b3231f;
    --purple: #5a2c86;
    --purple-dark: #451f6b;
    --orange: #f39a1f;
    --navy: #25295a;
    --white: #ffffff;
    --ink: #1d1d1d;
  }
  * { box-sizing: border-box; margin: 0; padding: 0; }
  html, body { width: 927px; height: 1200px; overflow: hidden; background: var(--white); }
  .flyer {
    position: relative; width: 927px; height: 1200px;
    font-family: "Jost", Arial, sans-serif; color: var(--white);
  }
  .photo { position: absolute; }
  .photo-boy { left: 0; top: 0; width: 310px; height: 412px; background: linear-gradient(180deg, #6d6a5e 0%, #d9d4c6 55%, #3b3a43 100%); }
  .photo-girl { left: 310px; top: 0; width: 308px; height: 412px; background: linear-gradient(160deg, #4a3a33 0%, #c9a68c 45%, #eae7e4 100%); }
  .photo-teens { left: 621px; top: 0; width: 306px; height: 412px; background: linear-gradient(180deg, #8b3b3a 0%, #c7b3a4 45%, #e9eaed 100%); }

  .intro { position: absolute; top: 412px; height: 156px; padding: 14px 12px 0 12px; font-size: 14.4px; line-height: 1.26; }
  .intro-invite { left: 0; width: 310px; background: var(--green); }
  .intro-chance { left: 310px; width: 308px; background: var(--blue); }
  .intro-join { left: 621px; width: 306px; background: var(--red); }

  .title-band {
    position: absolute; left: 0; top: 568px; width: 927px; height: 106px;
    background: linear-gradient(180deg, var(--purple) 0%, var(--purple-dark) 100%);
    display: flex; align-items: center; justify-content: center;
  }
  .title-band::before, .title-band::after {
    content: ""; position: absolute; left: 0; right: 0; height: 2px; background: rgba(255,255,255,0.55);
  }
  .title-band::before { top: 6px; }
  .title-band::after { bottom: 6px; }
  .title-band h1 { font-weight: 700; font-size: 34px; letter-spacing: 0.2px; }

  .map { position: absolute; left: 0; top: 676px; width: 311px; height: 286px; background: linear-gradient(135deg, #f3e3a8 0%, #f5c23a 50%, #d8dde6 100%); }
  .photo-school { position: absolute; left: 0; top: 968px; width: 311px; height: 232px; background: linear-gradient(180deg, #dfe4ea 0%, #c9c7c4 45%, #9a6a55 70%, #6e6a5c 100%); }

  .about {
    position: absolute; left: 311px; top: 676px; width: 616px; height: 452px;
    background: var(--orange); color: var(--ink); padding: 18px 14px 0 14px;
    font-size: 17px; line-height: 1.3;
  }
  .about h2 { font-size: 21px; font-weight: 700; letter-spacing: 0.3px; margin-bottom: 2px; }
  .about p + p { margin-top: 22px; }

  .footer {
    position: absolute; left: 311px; top: 1128px; width: 616px; height: 72px;
    background: var(--navy); display: flex; align-items: center; padding-left: 14px;
  }
  .footer-mark { width: 36px; height: 36px; border-radius: 50%; background: #e4b43a; flex: none; margin-right: 14px; }
  .footer-name { font-family: "Cinzel", Georgia, serif; font-size: 20px; line-height: 1.15; }
  .footer-sub { font-family: "Jost", Arial, sans-serif; font-size: 11.5px; letter-spacing: 0.4px; margin-top: 3px; }
</style>
</head>
<body>
<main class="flyer">
  <div class="photo photo-boy" role="img" aria-label="Smiling schoolboy in uniform holding a certificate"></div>
  <div class="photo photo-girl" role="img" aria-label="Smiling schoolgirl sitting among classmates"></div>
  <div class="photo photo-teens" role="img" aria-label="Two teenage students in white shirts standing together"></div>

  <p class="intro intro-invite">The board of directors of The Riverside Learning House at Tonle Prey invites you to our annual visit to Tonle Prey, Cambodia to help launch the new school year. The trip is open to everyone-you do not need to be a current donor to attend.</p>
  <p class="intro intro-chance">If you have been interested in visiting an educational project that works for hundreds of the poorest children in Cambodia, here is your chance. This school is a lifeline for these children and their families, providing education, transportation, uniforms, and two meals a day.</p>
  <p class="intro intro-join">Join us for the experience of a lifetime. You will be touched by the spirit of these children and their drive to learn. And, the local town of Siem Reap is the base from which to visit Angkor Wat, the World Heritage site that should not be missed.</p>

  <header class="title-band">
    <h1>The 2013 School Year Kick Off Tour October 1, 2013</h1>
  </header>

  <div class="map" role="img" aria-label="Map of Cambodia marking the school location near Siem Reap and Phnom Penh"></div>
  <div class="photo-school" role="img" aria-label="Two-storey school building with motorbikes parked in front"></div>

  <section class="about">
    <h2>ABOUT THE SCHOOL</h2>
    <p>Founded in April 2004 by Foster City, CA service club member Lars Movik, the Riverside Learning House at Tonle Prey provides a basic education aimed at reaching Cambodia's poorest youth. After having been both touched by the genuine kindness of the locals and yet unsettled by the widespread poverty suffered in the aftermath of the Vietnam War and Khmer Rouge era, Lars led efforts to turn an underutilized building into a thriving school in a region where education in neither compulsory nor affordable for the poorest families.</p>
    <p>In 2012, the school also reached the maximum enrollment of 345 students in twelve classes in grades K-9. The curriculum emphasizes English and all general subjects such as Khmer (the local language), math, science, and social studies.</p>
  </section>

  <footer class="footer">
    <span class="footer-mark"></span>
    <div>
      <div class="footer-name">The Riverside Learning House at Tonle Prey</div>
      <div class="footer-sub">Grades K-9. Supported by the Harbor Point Service Club of Foster City, CA</div>
    </div>
  </footer>
</main>
</body>
</html>
```